1. Can you describe what your company does?
-> We at M and P Orbex, we do Tube bending and its subassemblies. We can cater to different materials like Mild Steel, Stainless Steel, Aluminium and other non-ferrous material. We collaborate with our clients to make precise components to meet their industry requirements. At M&P Orbex we cater to smaller batches or high-volume requirements as per project needs.

2. Who are your target customers for the website?
-> Automotive, Road construction, warehouse equipment, Data centers, beverage equipment industry, electronics products manufacturers for making fixtures.
-> customers which require tubes and pipe bending, exhaust pipes, sheet metal parts

3. Do you have an existing domain name / website address?
-> This was an existing site: https://www.mandporbex.co.in/industry
-> using design.com I created this: https://sitelaunch.web/MandPOrbexpvtltd
But I am not very satisfied with the one I have created using design.com

4. In addition to a Home Page, which other pages / sections would you like your website to have:
About Us
Contact Us
Products / Services
Office / Mailing Address
Terms and Conditions

For each of the pages / sections you’d like to have, please provide the text (and images, if available) you would like to include.
-> Can you use the content that I have added on design.com : https://sitelaunch.web/MandPOrbexpvtltd

5. Which of the below are features and functionalities your website will need:
Image Gallery
Videos
Contact Form

6. Please provide the URLs for the social media profiles you'd like to link to the website.
-> Don't have one yet.

Coding

Coded - Design and coding required

```html
<!DOCTYPE html>
<html lang="en">
<head>
<meta charset="utf-8">
<title>M and P Orbex – Tube Bending</title>
<link href="https://fonts.googleapis.com/css2?family=Roboto+Condensed:wght@700&family=Inter:wght@400;500;600&display=swap" rel="stylesheet">
<style>
:root{
  --navy:#173f72;
  --blue:#1d4b8f;
  --royal:#2747a0;
  --section-blue:#2b4da3;
  --grey:#858889;
  --ink:#111;
  --text:#555;
  --white:#fff;
  --black:#000;
}
*{box-sizing:border-box;margin:0;padding:0}
html,body{width:1200px;height:4910px;overflow:hidden}
body{position:relative;background:var(--white);font-family:"Inter",sans-serif;color:var(--ink)}
.abs{position:absolute}
h1,h2,h3{font-family:"Roboto Condensed",sans-serif;font-weight:700}
.section-title{position:absolute;left:0;width:1200px;text-align:center;font-size:36px;letter-spacing:.3px}
.title-rule{position:absolute;width:70px;height:4px;background:var(--blue)}
.btn{position:absolute;display:flex;align-items:center;justify-content:center;background:var(--blue);color:#fff;font-family:"Roboto Condensed",sans-serif;font-weight:700;font-size:17px;border-radius:0 12px 0 12px;text-decoration:none}

/* header */
.topbar{position:absolute;left:0;top:0;width:1200px;height:51px}
.topbar-info{position:absolute;top:0;height:51px;display:flex;align-items:center;color:#fff;font-size:12px;gap:6px}
.topbar-sep{position:absolute;top:17px;width:1px;height:17px;background:#fff}
.logo-disc{position:absolute;left:120px;top:-40px;width:160px;height:208px;border-radius:0 0 80px 80px;background:#fff;display:flex;align-items:flex-end;justify-content:center;padding-bottom:40px;z-index:3}
.logo-name{font-family:"Inter",sans-serif;font-weight:500;font-size:15px;color:var(--blue)}
.nav{position:absolute;top:51px;left:0;width:1200px;height:59px;background:#fff}
.nav a{position:absolute;top:21px;font-size:13px;color:#111;text-decoration:none;font-weight:500}
.nav a.active{color:var(--blue)}

/* hero */
.hero-photo{position:absolute;left:0;top:110px;width:1200px;height:650px;
  background:linear-gradient(120deg,#5d6165 0%,#7b7f84 40%,#9aa0a6 65%,#4b6aa0 85%,#3a4c66 100%);
  clip-path:polygon(0 0,100% 0,100% 518px,50% 620px,0 518px)}
.hero-title{position:absolute;left:152px;top:252px;color:#fff;font-size:54px;line-height:70px}
.hero-sub{position:absolute;left:152px;top:413px;color:#fff;font-size:18px}

/* about */
.about-mark{position:absolute;left:168px;top:838px;width:337px;height:423px;display:flex;align-items:center;justify-content:center;font-family:"Roboto Condensed",sans-serif;font-weight:700;font-size:66px;color:var(--royal)}
.about-text{position:absolute;left:629px;width:422px;font-size:13px;line-height:21px;color:var(--text);text-align:justify}

/* services */
.service-card{position:absolute;width:437px;height:255px;border-radius:16px;background:var(--grey);color:#fff}
.service-card.featured{background:var(--royal)}
.service-photo{position:absolute;left:10px;top:12px;width:185px;height:231px;border-radius:12px;background:linear-gradient(135deg,#fafafa,#d9dadc 60%,#f4f4f4)}
.service-body{position:absolute;left:218px;top:34px;width:210px}
.service-body h3{font-size:18px;line-height:24px;margin-bottom:10px}
.service-body p{font-size:13px;line-height:20.5px;font-weight:500;max-height:123px;overflow:hidden}
.service-body .more{display:block;margin-top:12px;font-family:"Roboto Condensed",sans-serif;font-weight:700;font-size:13px;color:#fff;text-decoration:none}

/* industries */
.industries-bg{position:absolute;left:0;top:2130px;width:1200px;height:980px}
.industry-card{position:absolute;top:2400px;width:284px;height:503px;background:#fff;border-radius:14px;overflow:hidden;text-align:center}
.industry-photo{height:206px;border-radius:14px 14px 0 0}
.industry-card h3{font-size:18px;margin-top:34px}
.industry-card p{font-size:12.5px;line-height:18.8px;color:var(--text);padding:0 16px;margin-top:14px}

/* gallery */
.gallery-item{position:absolute;border-radius:14px}

/* contact */
.video{position:absolute;left:150px;top:3867px;width:418px;height:446px;border-radius:16px;background:linear-gradient(160deg,#c9d3dc,#e9eef2 45%,#6d8bb3 80%,#3d5a85)}
.field{position:absolute;border:1px solid #d8d8d8;border-radius:6px;font-size:11px;color:#555;padding:14px 12px 0}

/* footer */
.footer-name{position:absolute;left:150px;top:4740px;width:274px;text-align:center;color:#fff;font-size:26px}
.footer-heading{position:absolute;top:4560px;color:#fff;font-size:18px;font-weight:600}
.footer-rule{position:absolute;top:4590px;width:28px;height:2px;background:var(--blue)}
.footer-links{position:absolute;left:503px;top:4610px;list-style:none}
.footer-links li{font-size:12px;line-height:26px;color:#fff}
.footer-contact{position:absolute;left:773px;top:4612px;width:280px;color:#fff;font-size:12px;line-height:18px}
.footer-contact .label{margin-top:10px;font-size:11px}
.footer-contact .label:first-child{margin-top:0}
.footer-divider{position:absolute;left:177px;top:4804px;width:854px;height:1px;background:#777}
.copyright{position:absolute;left:0;top:4852px;width:1200px;text-align:center;color:#fff;font-size:12px;font-weight:500}
</style>
</head>
<body>

<!-- header -->
<header>
  <svg class="topbar" viewBox="0 0 1200 51" aria-hidden="true"><polygon points="286,0 1200,0 1200,51 320,51" fill="var(--navy)"/></svg>
  <div class="topbar-info" style="left:332px">
    <svg width="10" height="12" viewBox="0 0 10 12"><path d="M5 0a4 4 0 0 0-4 4c0 3 4 8 4 8s4-5 4-8a4 4 0 0 0-4-4zm0 5.5A1.5 1.5 0 1 1 5 2.5a1.5 1.5 0 0 1 0 3z" fill="#fff"/></svg>
    B14 'R' Block MIDC Talawade, Pune- 411062 India
  </div>
  <span class="topbar-sep" style="left:662px"></span>
  <div class="topbar-info" style="left:684px">
    <svg width="13" height="10" viewBox="0 0 13 10"><rect x=".6" y=".6" width="11.8" height="8.8" rx="1" fill="none" stroke="#fff" stroke-width="1.2"/><path d="M1 1l5.5 4.5L12 1" fill="none" stroke="#fff" stroke-width="1.2"/></svg>
    info@mandporbex.co.in
  </div>
  <span class="topbar-sep" style="left:908px"></span>
  <div class="topbar-info" style="left:932px">
    <svg width="11" height="11" viewBox="0 0 11 11"><path d="M2.2 0l2 2.4-1 1.4a7 7 0 0 0 4 4l1.4-1 2.4 2-1.2 2.2C4.8 10.6.4 6.2 0 1.2z" fill="#fff"/></svg>
    +91-9123456780
  </div>
  <div class="logo-disc"><span class="logo-name">M and P Orbex</span></div>
  <nav class="nav">
    <a class="active" style="left:326px" href="#">Home</a>
    <a style="left:394px" href="#">About Us</a>
    <a style="left:484px" href="#">Our Services</a>
    <a style="left:598px" href="#">Machines and Certifications</a>
    <a style="left:808px" href="#">Industries We Serve</a>
    <a style="left:966px" href="#">Our Products</a>
  </nav>
</header>

<!-- hero -->
<section class="hero">
  <div class="hero-photo" role="img" aria-label="Close-up of a tube bending machine shaping stainless steel pipes"></div>
  <svg class="abs" style="left:0;top:620px" width="1200" height="140" viewBox="0 620 1200 140" aria-hidden="true">
    <polygon points="0,628 600,730 1200,628 1200,638 600,756 0,638" fill="var(--navy)"/>
  </svg>
  <h1 class="hero-title">M&amp;P is a Perfect Fit for<br>Your Tube Bending Needs!</h1>
  <p class="hero-sub">Engineering Flow, Forming Future</p>
  <a class="btn" style="left:152px;top:461px;width:147px;height:44px" href="#">Get Started</a>
</section>

<!-- about -->
<section class="about">
  <div class="about-mark">M&amp;P Orbex</div>
  <h2 class="abs" style="left:629px;top:838px;font-size:36px">ABOUT US</h2>
  <span class="title-rule" style="left:629px;top:893px"></span>
  <p class="about-text" style="top:921px">We at M and P Orbex, are proud to be expert in Tube bending and its subassemblies. We can cater to different materials like Mild Steel, Stainless Steel, Aluminium and other non-ferrous material.</p>
  <p class="about-text" style="top:1004px">We collaborate with our clients to make precise components to meet your industry requirements. At M&amp;P Orbex we cater to smaller batches or high-volume requirements as per project needs. Our experienced team of engineers works diligently and efficiently to develop the products which enhances the quality, optimizes manufacturing process and reduces the overall cost of the product for the customer.</p>
  <a class="btn" style="left:629px;top:1179px;width:144px;height:44px" href="#">Read More</a>
</section>

<!-- services -->
<section class="services">
  <h2 class="section-title" style="top:1364px">OUR SERVICES</h2>
  <span class="title-rule" style="left:565px;top:1419px"></span>

  <article class="service-card featured" style="left:150px;top:1469px">
    <div class="service-photo" role="img" aria-label="Two bent steel exhaust tubes"></div>
    <div class="service-body"><h3>Tube and Pipe Bending</h3>
      <p>We specialize in Tube and Pipe Bending We handle a variety of industrial projects with a wide scope of customer needs. We offer custom bending solutions</p>
      <a class="more" href="#">Read More</a></div>
  </article>
  <article class="service-card" style="left:613px;top:1469px">
    <div class="service-photo" role="img" aria-label="Steel tube with formed end"></div>
    <div class="service-body"><h3>Tube End Forming</h3>
      <p>Our tube end forming service is second to none, providing precision and customization for all your project needs. Our team of experts will provide you with precise and</p>
      <a class="more" href="#">Read More</a></div>
  </article>
  <article class="service-card" style="left:150px;top:1751px">
    <div class="service-photo" role="img" aria-label="Exhaust pipe wrapped in thermal insulation"></div>
    <div class="service-body"><h3>Thermal Insulation</h3>
      <p>We offer comprehensive automotive insulation solutions, including Thermal Insulation for exhaust pipes. Our expert team uses the latest techniques and</p>
      <a class="more" href="#">Read More</a></div>
  </article>
  <article class="service-card" style="left:613px;top:1751px">
    <div class="service-photo" role="img" aria-label="Cylindrical stainless steel exhaust silencer"></div>
    <div class="service-body"><h3>Exhaust Muffler and Silencers</h3>
      <p>Reducing noise and increasing comfort is our top priority with our Exhaust Silencer and mufflers. Our exhaust mufflers are built to</p>
      <a class="more" href="#">Read More</a></div>
  </article>
</section>

<!-- industries -->
<section class="industries">
  <svg class="industries-bg" viewBox="0 0 1200 980" role="img" aria-label="Blue-tinted background of an engineer on a factory floor">
    <defs><linearGradient id="indGrad" x1="0" y1="0" x2="1" y2="1">
      <stop offset="0" stop-color="#2f4f9c"/><stop offset=".5" stop-color="#2b4da3"/><stop offset="1" stop-color="#25449a"/></linearGradient></defs>
    <polygon points="0,126 600,0 1200,126 1200,136 600,12 0,136" fill="var(--grey)"/>
    <polygon points="0,146 600,22 1200,146 1200,960 600,872 0,960" fill="url(#indGrad)"/>
    <polygon points="0,926 600,846 1200,926 1200,936 600,858 0,936" fill="var(--grey)"/>
    <polygon points="0,916 600,836 1200,916 1200,926 600,846 0,926" fill="#fff"/>
  </svg>
  <h2 class="section-title" style="top:2282px;color:#fff">INDUSTRIES WE SERVE</h2>
  <span class="title-rule" style="left:565px;top:2336px;background:#fff"></span>

  <article class="industry-card" style="left:150px">
    <div class="industry-photo" role="img" aria-label="Engine assembly line with workers" style="background:linear-gradient(160deg,#d6dbe0,#9ea6ae 50%,#5f6670)"></div>
    <h3>Automotive</h3>
    <p>We specialize in the manufacturing of high-quality exhaust pipes, muffler, handlebars, cross bars, swing arms, air intake pipes for automobiles. We are proud to offer a wide range of products that will meet your every need and exceed your expectations. Contact us today to learn more about our products and services.</p>
  </article>
  <article class="industry-card" style="left:459px">
    <div class="industry-photo" role="img" aria-label="Engineers at a road construction site at sunset" style="background:linear-gradient(160deg,#f0d6a8,#c89a62 45%,#6d6a63)"></div>
    <h3>Road Construction</h3>
    <p>We understand the importance of reliable and top-quality products for road construction projects. That's why we are dedicated to providing the most advanced manufacturing solutions for exhaust pipes, mufflers, and railing systems, as well as partnering with road construction companies to offer the highest quality products available.</p>
  </article>
  <article class="industry-card" style="left:766px">
    <div class="industry-photo" role="img" aria-label="Crane lifting a bundle of steel pipes" style="background:linear-gradient(170deg,#8fb3d8,#c8d2dc 45%,#d8a23c 75%,#6b6d70)"></div>
    <h3>Warehousing Equipment</h3>
    <p>Reliability and durability are key when it comes to Warehousing Equipment. That's why we offer a wide range of high-quality chassis and driver cabins, exhaust pipes, mufflers, air intake pipes to accommodate your specific requirements.</p>
  </article>
</section>

<!-- gallery -->
<section class="gallery">
  <h2 class="section-title" style="top:3122px">PRODUCTS GALLERY</h2>
  <span class="title-rule" style="left:565px;top:3178px"></span>
  <div class="gallery-item" role="img" aria-label="Red mower deck frame" style="left:150px;top:3233px;width:252px;height:246px;background:linear-gradient(150deg,#e8483a,#c9302a 50%,#2d3d4f)"></div>
  <div class="gallery-item" role="img" aria-label="Steel welding fixture with clamps" style="left:419px;top:3233px;width:253px;height:246px;background:linear-gradient(150deg,#6b6c6a,#3e3f3d 55%,#8a8b87)"></div>
  <div class="gallery-item" role="img" aria-label="Row of electrical control cabinets" style="left:690px;top:3233px;width:360px;height:246px;background:linear-gradient(90deg,#a6a9a4,#d4d5d0 40%,#9c9e99)"></div>
  <div class="gallery-item" role="img" aria-label="Yellow steel block mould frame" style="left:150px;top:3500px;width:361px;height:245px;background:linear-gradient(160deg,#5a5a52,#e2b51c 45%,#c79a10 75%,#7b7a72)"></div>
  <div class="gallery-item" role="img" aria-label="Welded steel fixture on a workshop floor" style="left:528px;top:3500px;width:520px;height:245px;background:linear-gradient(160deg,#9c9891,#6e6b66 50%,#a8a49c)"></div>
</section>

<!-- contact -->
<section class="contact">
  <div class="video" role="img" aria-label="Engineering team working at computers in the design office"></div>
  <svg class="abs" style="left:331px;top:4062px" width="56" height="56" viewBox="0 0 56 56" aria-label="Play video"><circle cx="28" cy="28" r="28" fill="var(--blue)"/><polygon points="22,17 40,28 22,39" fill="#fff"/></svg>
  <h2 class="abs" style="left:613px;top:3888px;font-size:36px">GET IN TOUCH</h2>
  <span class="title-rule" style="left:613px;top:3945px"></span>
  <div class="field" style="left:617px;top:3976px;width:208px;height:40px">First Name</div>
  <div class="field" style="left:840px;top:3976px;width:208px;height:40px">Last Name</div>
  <div class="field" style="left:617px;top:4029px;width:208px;height:40px">Email</div>
  <div class="field" style="left:840px;top:4029px;width:208px;height:40px">Phone</div>
  <div class="field" style="left:617px;top:4083px;width:431px;height:135px">Message</div>
  <a class="btn" style="left:627px;top:4246px;width:146px;height:44px" href="#">Send Now</a>
</section>

<!-- footer -->
<footer>
  <svg class="abs" style="left:0;top:4400px" width="1200" height="510" viewBox="0 4400 1200 510" aria-hidden="true">
    <polygon points="0,4538 600,4412 1200,4538 1200,4548 600,4440 0,4548" fill="var(--navy)"/>
    <polygon points="0,4553 600,4448 1200,4553 1200,4910 0,4910" fill="var(--black)"/>
  </svg>
  <div class="footer-name">M and P Orbex</div>
  <h3 class="footer-heading" style="left:503px">More Info</h3>
  <span class="footer-rule" style="left:503px"></span>
  <ul class="footer-links">
    <li>Home</li><li>About Us</li><li>Our Services</li><li>Machines and Certifications</li><li>Industries We Serve</li><li>Our Products</li><li>Contact Us</li>
  </ul>
  <h3 class="footer-heading" style="left:773px">Contact Us</h3>
  <span class="footer-rule" style="left:773px"></span>
  <div class="footer-contact">
    <p class="label">ADDRESS</p>
    <p>&#9679; B14 'R' Block MIDC Talawade, Pune- 411062 India</p>
    <p class="label">PHONE</p>
    <p>+91-9123456780</p>
    <p class="label">EMAIL</p>
    <p>info@mandporbex.co.in</p>
  </div>
  <span class="footer-divider"></span>
  <p class="copyright">© copyrights 2026 &nbsp;M and P Orbex I Rights Reserved</p>
</footer>

</body>
</html>
```